GUARANTEED WordPress design needed for a sassy, confident charisma coach!

We need a website design for Marla Penrick's brand new, responsive, Wordpress website.
Marla is a trainer / coach who teaches people how to be more charismatic and runs events, publishes video courses and has an ongoing video blog. Her old website is here: www.marlapenrick.co.uk ... but it's now time to have a much better site!
We have a strong idea about the technical components of the website, but we need a designer's eye to create a great style for the site (and provide layered PSD files which our developers will then convert to HTML and CSS).
Marla's brand is sassy, brave, warm and confident. The videos on her existing site give quite a good feel for her personality. We need a clean, stylish and compelling page that isn't too corporate and captures her personality. Every element needs to feel coherent, from fonts and headings to colours and spacing.
The following sites are not exactly what Marla wants (and certainly aren't right in terms of colours) but they give you an idea of the kind of people she is competing against and the area she is operating in:
http://www.tessa-broughley.example/
http://rowanfelsby.example/
Ideally, you will have done something similar and be able to key in on exactly the kind of thing we want: we're not looking to reinvent the wheel. Hopefully you won't mind tweaking a few things if you are close to what we need.
More detail is provided in the word document attached. But in a nutshell we need: a banner, footer, sign-up strap, menu bar, signature and 4 different basic page types. We want bursts of bright colours, contrasted with black and white if possible - sorry we can't be more specific than that...
The word doc also contains some amateur mock-ups as well (the images are also just mockups at this stage) - but although these give a general sense of the structure what we are looking for, we are clearly not designers...so please help! We need a designer's touch!
Kind regards,
Corin
PS The layered PSD versions of the mockup files are available on Cloudvantre: https://files.cloudvantre.example/sh/k72pqa4w1zbtmrd/QXvenlr8Ty3PwMiU6Hs2kYfDb?dl=0
Target Market(s)
Entrepreneurs who need to sell themselves.
Number of Pages Required
4 page

```html
<!DOCTYPE html>
<html lang="en">
<head>
<meta charset="utf-8">
<title>About the charisma coach – Marla Penrick</title>
<link href="https://fonts.googleapis.com/css2?family=Roboto+Condensed:wght@400;700&family=Roboto:wght@300;400&display=swap" rel="stylesheet">
<style>
:root{
  --brand-red:#c8102e;
  --nav-active:#de3b1e;
  --ink:#111;
  --body-text:#3a3a3a;
  --page-grey:#e6e6e6;
  --panel:#fff;
  --icon-dark:#3a3a3a;
  --share-sky:#2ba6de;
  --share-slate:#34465d;
  --share-navy:#3b5998;
  --share-grey:#7e8c8d;
  --share-ash:#8e9a9b;
  --share-coral:#f26d50;
}
*{box-sizing:border-box;margin:0;padding:0}
html,body{width:1200px;height:1173px;overflow:hidden}
body{position:relative;background:var(--page-grey);font-family:"Roboto",sans-serif;color:var(--body-text)}

.site-header{position:absolute;left:0;top:0;width:1200px;height:100px;background:var(--panel)}
.brand{position:absolute;left:116px;top:32px;font-family:"Roboto Condensed",sans-serif;font-weight:700;font-size:28px;color:var(--ink);letter-spacing:.2px}
.social{position:absolute;left:574px;top:38px;display:flex;gap:10px;list-style:none}
.social li{width:28px;height:28px;border-radius:50%;background:var(--icon-dark)}
.search{position:absolute;left:846px;top:32px;width:245px;height:39px;border:3px solid var(--icon-dark);background:#fff}
.search span{position:absolute;left:17px;top:9px;font-size:13px;color:#555}
.search svg{position:absolute;right:9px;top:8px}

.main-nav{position:absolute;left:0;top:100px;width:1200px;height:43px;background:var(--brand-red)}
.main-nav ul{list-style:none;position:relative;height:100%}
.main-nav li{position:absolute;top:0;height:43px;line-height:43px;text-align:center;font-family:"Roboto Condensed",sans-serif;font-weight:700;font-size:15px;color:#fff;border-left:1px solid rgba(255,255,255,.18)}
.main-nav li.first{border-left:none}
.main-nav li.is-active{background:var(--nav-active)}

.hero{position:absolute;left:0;top:143px;width:1200px;height:347px;background:linear-gradient(160deg,#f1f1ef 0%,#e4e4e2 55%,#d9d9d6 100%)}
.hero-figure{position:absolute;left:645px;top:143px;width:486px;height:381px;background:radial-gradient(ellipse at 35% 55%,rgba(226,35,40,.85) 0%,rgba(226,35,40,.55) 35%,rgba(226,35,40,0) 70%)}
.hero-title{position:absolute;left:240px;top:243px;width:300px;text-align:center;font-family:"Roboto Condensed",sans-serif;font-weight:700;font-size:30px;line-height:37px;color:var(--ink);white-space:nowrap}

.share-bar{position:absolute;left:74px;top:491px;width:40px;list-style:none}
.share-bar li{position:relative;height:43.5px;display:flex;flex-direction:column;align-items:center;justify-content:center;color:#fff;font-size:8px}
.share-bar .dot{width:14px;height:14px;border-radius:50%;background:#fff;margin-bottom:2px}
.share-sky{background:var(--share-sky)}
.share-slate{background:var(--share-slate)}
.share-navy{background:var(--share-navy)}
.share-grey{background:var(--share-grey)}
.share-ash{background:var(--share-ash)}
.share-coral{background:var(--share-coral)}

.story{position:absolute;left:113px;top:457px;width:645px;height:716px;background:var(--panel)}
.sidebar{position:absolute;left:783px;top:524px;width:311px;height:649px;background:var(--panel)}
h2{font-family:"Roboto Condensed",sans-serif;font-weight:700;font-size:29px;color:var(--brand-red);line-height:1}
.story h2{position:absolute;left:34px;top:40px}
.sidebar h2{position:absolute;left:34px;top:32px}
p{font-weight:300;font-size:10.6px;line-height:20px}
.story .intro{position:absolute;left:34px;top:95px;width:566px}
.story .intro p+p{margin-top:20px}
.story-photo{position:absolute;left:29px;top:302px;width:570px;height:318px;background:linear-gradient(135deg,#b7a38e 0%,#7c6a5e 40%,#3d3535 70%,#7a2b38 100%)}
.story .outro{position:absolute;left:34px;top:648px;width:566px}
.sidebar .copy{position:absolute;left:38px;top:87px;width:218px}
.sidebar .copy p+p{margin-top:20px}
</style>
</head>
<body>
<header class="site-header">
  <div class="brand">Marla Penrick ltd</div>
  <ul class="social" aria-label="Social profiles">
    <li></li><li></li><li></li><li></li><li></li><li></li><li></li>
  </ul>
  <div class="search">
    <span>Enter your keyword...</span>
    <svg width="20" height="20" viewBox="0 0 20 20"><circle cx="8" cy="8" r="6.2" fill="none" stroke="#222" stroke-width="2"/><line x1="12.6" y1="12.6" x2="18.5" y2="18.5" stroke="#222" stroke-width="2.4" stroke-linecap="round"/></svg>
  </div>
</header>

<nav class="main-nav">
  <ul>
    <li class="first" style="left:100px;width:156px">HOME</li>
    <li style="left:256px;width:167px">VENTS</li>
    <li style="left:423px;width:168px">WORK WITH ME</li>
    <li style="left:591px;width:167px">CORPORATE</li>
    <li class="is-active" style="left:758px;width:168px">ABOUT</li>
    <li style="left:926px;width:160px">CONTACT</li>
  </ul>
</nav>

<div class="hero" role="img" aria-label="Light paved stone ground photographed from above"></div>
<div class="hero-figure" role="img" aria-label="Marla in a red dress and black heels, sitting and leaning back with a laugh"></div>
<h1 class="hero-title">About the<br>charisma coach</h1>

<ul class="share-bar" aria-label="Share this page">
  <li class="share-sky"><span class="dot"></span>15.7K</li>
  <li class="share-slate"><span class="dot"></span></li>
  <li class="share-navy"><span class="dot"></span>123K</li>
  <li class="share-grey"><svg width="18" height="13" viewBox="0 0 18 13"><rect x="0.5" y="0.5" width="17" height="12" fill="#fff"/><polyline points="1,1 9,7 17,1" fill="none" stroke="#7e8c8d" stroke-width="1.4"/></svg></li>
  <li class="share-ash"><svg width="18" height="16" viewBox="0 0 18 16"><rect x="4" y="0" width="10" height="5" fill="#fff"/><rect x="0" y="5" width="18" height="7" rx="1" fill="#fff"/><rect x="4" y="9" width="10" height="7" fill="#fff" stroke="#8e9a9b"/></svg></li>
  <li class="share-coral"><svg width="16" height="16" viewBox="0 0 16 16"><rect x="6" y="0" width="4" height="16" fill="#fff"/><rect x="0" y="6" width="16" height="4" fill="#fff"/></svg><span>2.6M</span></li>
</ul>

<main class="story">
  <h2>My story</h2>
  <div class="intro">
    <p>Exposed neither pressed so cottage as proceed at offices. Nay they gone sir game four. Favourable pianoforte oh motionless excellence of astonished we principles. Warrant present garrets limited cordial in inquiry to. Supported me sweetness behaviour shameless excellent so arranging.</p>
    <p>Remain lively hardly needed at do by. Two you fat downs fanny three. True mr gone most at. Dare as name just when with it body. Travelling inquietude she increasing off impossible the. Cottage be noisier looking to we promise on. Disposal to kindness appetite diverted learning of on raptures. Betrayed any may returned now dashwood formerly. Balls way delay shy boy man views.</p>
  </div>
  <div class="story-photo" role="img" aria-label="Marla relaxing on a patterned sofa with cushions, cuddling her black and white dog"></div>
  <div class="outro">
    <p>Exposed neither pressed so cottage as proceed at offices. Nay they gone sir game four. Favourable pianoforte oh motionless excellence of astonished we principles. Warrant present garrets limited cordial in inquiry to. Supported me sweetness behaviour shameless excellent so arranging.</p>
  </div>
</main>

<aside class="sidebar">
  <h2>The charisma code</h2>
  <div class="copy">
    <p>Ecstatic advanced and procured civility not absolute put continue. Overcame breeding or my concerns removing desirous so absolute. My melancholy unpleasing imprudence considered in advantages so impression. Almost unable put piqued talked likely houses her met. Met any nor may through resolve entered. An mr cause tried oh do shade happy.</p>
    <p>Is we miles ready he might going. Own books built put civil fully blind fanny. Projection appearance at of admiration no. As he totally cousins warrant besides ashamed do. Therefore by applauded acuteness supported affection it. Except had sex limits county enough the figure former add. Do sang my he next mr soon. It merely waited do unable.</p>
    <p>From they fine john he give of rich he. They age and draw mrs like. Improving end distrusts may instantly was household applauded incommode. Why kept very ever home mrs. Considered sympathize ten uncommonly occasional assistance sufficient not. Letter of on become he tended active enable to. Vicinity relation sensible</p>
  </div>
</aside>
</body>
</html>
```